既にロゴはありますので、ロゴ(色は変更可能)に合わせたページのデザインをお願いします。
ロゴはこちらのコーポレートサイトのヘッダー左上にある「クモマーケット」になります。
https://kumomarket.co.jp/

◆トップページに乗せたい要素
・全ページ共通のヘッダーとフッター
・アイキャッチ画像(出張買取と宅配買取により全国に対応している旨を伝えたいです)
・新着情報(ブログ記事)
・買取事例
・買取品目 (後述)
・特化した別サイトへのリンク画像
・簡単な買取の流れ
・査定、依頼、問い合わせへのリンク

◆業務の範囲
デザイン

◆対応ページ数
レスポンシブデザインのため、2ページ(PC1枚、スマホ1枚)
予算の都合上トップページのみの依頼ですが、内容次第では下記サイトマップにあるページも追加依頼を考えております。

<サイトマップ>
〇トップページ ←今回の案件
〇買取の流れ(出張買取、宅配買取、店頭買取の流れ)
〇買取品目・ブランド一覧
〇各品目、各ブランドの個別ページ
〇買取実績一覧
〇買取実績
〇無料査定(電話番号、TALKA@へのリンクボタン、メールフォーム)
〇買取依頼フォーム(出張、宅配、店頭)
〇よくある質問
〇記事一覧
〇記事ページ
〇お問い合わせ
〇プライバシーポリシー
〇会社概要
〇プライバシーポリシー(新デザインに合わせヘッダーフッターの変更程度)

◆現在のサイト※このサイトの全面的なリニューアルです。
https://kumo-market.com/

◆他のジャンル特化のサイト

アウトドア・スポーツ用品
https://sorano-hara.shop/

トイガン
https://gun-kumomarket.com/

楽器
https://mimoza-oto.com/

電動工具
https://tool-kumomarket.com/

工場機械・車両
https://kumomarket-machine.com/

◆こんなサイトの雰囲気にしたい
多岐に渡る買取品目のため、年齢、性別などを選ばないすっきりとしたデザインを希望しています。

◆参考サイト
https://www.pinoru-reuse.com
https://tobimaru.net/sell/
https://kaerune.net/
https://www.yorozuhiroba.com/
http://fennick-trails.com/
https://kanamono-sato.co.jp/
https://www.otohibiki-ya.com/
https://pellwick.jp/

◆期待する効果:問い合わせ件数UP
◆スマホ対応の有無:レスポンシブWebデザイン

◆買取品目 例

〇家電・AV機器・カメラ
テレビ、プロジェクター、冷蔵庫、洗濯機、掃除機、高圧洗浄機、ミシン、エアコン、空気清浄機
オーディオ、コンポ、サウンポケ、スピーカー、ヘッドフォン
BDレコーダー、カメラ、レンズ、三脚、望遠鏡

〇スマホ・PC関連
Velio、Velitab、スマートフォン、タブレット、パソコン、モニター、PCソフト、スキャナー、プリンター

〇インテリア・家具・住宅設備
テレビ台、チェア、ソファ、ベッド
照明器具、住宅建材、インテリア雑貨、食器、調理器具

〇カー用品 (工具、機械はツールクモへ)
ヘルメット、タイヤ、ホイール、カーナビ、車載工具、自動車用機械

〇ホビー (トイガンは当社Webサイトのガンクモへ)
フィギュア、ドール、トレーディングカード、ブリキ・超合金、ソフビ、プラモデル、ミニカー、ラジコン、鉄道模型
トイガン、ドローン、全自動麻雀卓、将棋駒、アイドル・アニメ

〇楽器(当社Webサイトのミモザオトへ)
ギター、ベース、ドラム、サックス、ピアノ、打楽器、弦楽器、管楽器、民族楽器、和楽器、アンプ、音楽機材、ヘッドフォン

〇スポーツ・レジャー・アウトドア (当社Webサイトのソラノハラへ)
キャンプ、登山、釣具、ゴルフ、乗馬用品、自転車
ダイビング、スノーボード
カヌー、バックパック、アウトドアウェア

〇電動工具・機械(当社Webサイトのツールクモへ)
DIY工具、プロ用工具、発電機、溶接機、コンプレッサー、高圧洗浄機
工具箱

〇ビューティ・ヘルスケア
美顔器

〇ブランドファッション
メンズ服、レディース服、時計、貴金属、アクセサリー、バッグ、財布、革小物

〇美術品・雑貨
絵画、貨幣、古銭、切手、工芸品、民芸品、骨董品、彫刻仏像、刀、鎧、兜
万年筆

〇店舗・オフィス用品(一部クモマシンへ)
複合機、券売機、業務用冷蔵庫、製氷機、製麺機、寿司ロボット

〇法人用機械買取(クモマシンへ)
旋盤、溶接機、工作機械、印刷・製本機、食品厨房機器
フォークリフト、タイヤチェンジャー、油圧ショベル、クレナ、ダンプ
耕運機、トラクター、コンバイン、オシロスコープ、顕微鏡
https://kumo-market.com/
◆納品方法
PSDデータ
それぞれレイヤーを残した状態でお願い致します。
また、文字のアウトライン前と後のものを用意して頂けると助かります。
納品についてはPSDの他、aiデータでも受け付けします。宜しくお願い致します。

デザインについては好みがあるのでどれにするか迷いましたが、決めさせて頂いたデザインとその説明が弊社にとって一番しっくりとくるものでした。

今回は弊社の依頼にご応募いただきましてありがとうございました。

また何か別の機会がありましたらよろしくお願い致します。

```html
<!DOCTYPE html>
<html lang="ja">
<head>
<meta charset="utf-8">
<title>クモマーケット｜全国から買取可能</title>
<link href="https://fonts.googleapis.com/css2?family=Noto+Sans+JP:wght@400;500;700;900&family=Roboto:wght@500;700;900&display=swap" rel="stylesheet">
<style>
:root{
  --red:#d7282f;
  --red-dark:#b51d23;
  --yellow:#ffe45a;
  --yellow-soft:#fff7d6;
  --ink:#2b2b2b;
  --sub:#6b6b6b;
  --line:#e3e3e3;
  --grey-bg:#f4f4f4;
  --green:#2fb54a;
  --blue:#4d7fb8;
  --blue-soft:#e8eef5;
  --dark:#1f1f1f;
  --white:#fff;
}
*{box-sizing:border-box;margin:0;padding:0}
html,body{width:1200px;height:3624px;overflow:hidden}
body{font-family:"Noto Sans JP",sans-serif;color:var(--ink);background:var(--white);font-size:13px;line-height:1.6}
a{color:inherit;text-decoration:none}
.wrap{width:960px;margin:0 auto;position:relative}
.num{font-family:"Roboto","Noto Sans JP",sans-serif}

/* header */
.site-header{height:100px;border-bottom:1px solid var(--line)}
.header-top{display:flex;align-items:center;height:60px;width:1120px;margin:0 auto}
.logo{display:flex;align-items:center;gap:12px}
.logo-name{font-size:28px;font-weight:900;color:var(--red);letter-spacing:.02em}
.logo-tag{font-size:10px;color:var(--sub);line-height:1.4}
.header-tel{margin-left:auto;display:flex;align-items:center;gap:8px}
.header-tel .num{font-size:26px;font-weight:700;color:var(--ink)}
.header-tel small{display:block;font-size:9px;color:var(--sub);line-height:1.2}
.header-btns{display:flex;gap:8px;margin-left:22px}
.btn-pill{display:flex;align-items:center;gap:6px;height:34px;padding:0 16px;border-radius:17px;font-size:12px;font-weight:700;color:var(--white)}
.btn-pill.red{background:var(--red)}
.btn-pill.green{background:var(--green)}
.global-nav{display:flex;width:1120px;margin:0 auto;height:40px}
.global-nav a{flex:1;display:flex;align-items:center;justify-content:center;font-size:13px;font-weight:500;border-left:1px solid var(--line)}
.global-nav a:last-child{border-right:1px solid var(--line)}
.global-nav a.is-current{background:var(--red);color:var(--white)}

/* hero */
.hero{position:relative;height:420px;background:var(--yellow);overflow:hidden}
.hero-visual{position:absolute;inset:0;background:
  radial-gradient(ellipse 380px 200px at 50% 48%,var(--yellow) 60%,transparent 100%),
  linear-gradient(90deg,#c9a66b 0%,#e9d6a8 14%,var(--yellow) 30%,var(--yellow) 70%,#e8c9a0 86%,#b7573f 100%)}
.hero-copy{position:absolute;left:50%;top:52px;transform:translateX(-50%);text-align:center;width:560px}
.hero-title{font-size:50px;font-weight:900;letter-spacing:.04em;line-height:1.2}
.hero-badges{display:flex;justify-content:center;gap:26px;margin-top:24px}
.hero-badge{display:flex;align-items:center;gap:10px}
.badge-circle{width:76px;height:76px;border-radius:50%;background:var(--red);color:var(--white);font-weight:900;font-size:15px;line-height:1.2;display:flex;align-items:center;justify-content:center;text-align:center}
.badge-circle.blue{background:var(--blue)}
.badge-text{font-size:22px;font-weight:900;color:var(--red);line-height:1.3;text-align:left}
.badge-text.blue{color:var(--blue)}
.hero-lead{margin-top:22px;font-size:16px;font-weight:700;line-height:1.7}

/* section heads */
.sec-title{text-align:center;font-size:28px;font-weight:900;letter-spacing:.06em}
.sec-title::after{content:"";display:block;width:40px;height:3px;background:var(--red);margin:10px auto 0}
.sec-lead{text-align:center;font-size:12px;color:var(--sub);margin-top:12px}
.btn-more{display:flex;align-items:center;justify-content:center;gap:10px;width:180px;height:40px;margin:0 auto;border-radius:20px;background:var(--dark);color:var(--white);font-size:12px;font-weight:700}

/* news */
.news{height:340px;padding-top:50px}
.news .wrap{display:flex;gap:40px}
.news-head{width:170px;padding-top:30px;font-size:24px;font-weight:900}
.news-list{flex:1;list-style:none}
.news-list li{display:flex;align-items:center;gap:12px;height:50px;border-bottom:1px solid var(--line);font-size:12px}
.news-date{display:inline-block;width:92px;height:20px;line-height:20px;text-align:center;border-radius:10px;background:#bdbdbd;color:var(--white);font-size:11px}
.news-cat{display:inline-block;width:80px;height:20px;line-height:18px;text-align:center;border:1px solid var(--red);color:var(--red);font-size:11px;border-radius:2px}
.news .btn-more{margin-top:26px}

/* results */
.results{height:500px;background:var(--yellow-soft);padding-top:44px}
.result-slider{display:flex;align-items:center;gap:14px;margin-top:28px}
.slide-arrow{width:28px;height:28px;border-radius:50%;background:var(--white);box-shadow:0 1px 3px rgba(0,0,0,.15);display:flex;align-items:center;justify-content:center;flex:none}
.result-cards{display:flex;gap:16px;flex:1}
.result-card{flex:1;background:var(--white);box-shadow:0 1px 4px rgba(0,0,0,.08)}
.result-img{height:150px}
.result-body{padding:10px 12px 12px}
.result-date{font-size:10px;color:var(--sub)}
.result-name{font-size:12px;line-height:1.5;height:36px;overflow:hidden}
.result-price{display:flex;justify-content:space-between;align-items:baseline;border-top:1px solid var(--line);padding-top:6px;margin-top:6px;font-size:10px;color:var(--sub)}
.result-price .num{font-size:22px;font-weight:900;color:var(--red)}
.result-price .num small{font-size:12px}
.dots{display:flex;justify-content:center;gap:8px;margin:18px 0 20px}
.dots span{width:7px;height:7px;border-radius:50%;background:#cfcfcf}
.dots span.on{background:var(--red)}

/* items */
.items{height:720px;padding-top:56px}
.item-grid{display:grid;grid-template-columns:repeat(4,1fr);gap:16px;margin-top:30px}
.item-card{border:1px solid var(--line);background:var(--white);height:168px}
.item-label{display:flex;align-items:center;gap:7px;height:34px;padding:0 10px;border-bottom:1px solid var(--line);font-size:12px;font-weight:700}
.item-label i{width:14px;height:14px;border-radius:50%;background:var(--red);flex:none}
.item-body{display:flex;gap:8px;padding:10px}
.item-words{flex:1;font-size:10.5px;color:var(--sub);line-height:1.6}
.item-img{width:92px;height:110px;flex:none}
.items .btn-more{margin-top:30px}

/* sister sites */
.sites{height:330px;background:#fbeeea;padding-top:36px}
.sites-head{text-align:center;font-size:17px;font-weight:900;color:var(--red)}
.sites-head span{font-size:12px;color:var(--ink);font-weight:500;margin-left:10px}
.site-row{display:flex;gap:14px;margin-top:22px}
.site-card{flex:1}
.site-img{height:120px}
.site-name{margin-top:10px;height:40px;display:flex;align-items:center;justify-content:center;gap:6px;background:var(--white);font-size:17px;font-weight:900;color:var(--red)}
.site-name i{width:10px;height:10px;background:var(--red)}
.site-caption{margin-top:6px;text-align:center;font-size:11px;color:var(--sub);line-height:1.5}

/* flow */
.flow{height:520px;padding-top:44px}
.flow-tabs{display:flex;margin-top:24px}
.flow-tab{flex:1;height:36px;display:flex;align-items:center;justify-content:center;font-size:14px;font-weight:700}
.flow-tab.is-active{background:var(--blue-soft);color:var(--red)}
.flow-tab.other{background:var(--blue);color:var(--white)}
.flow-steps{background:var(--blue-soft);display:flex;gap:10px;padding:22px 18px 24px}
.flow-step{flex:1;position:relative}
.step-head{display:flex;flex-direction:column;align-items:center;justify-content:center;height:50px;background:var(--white);font-weight:700;font-size:13px;clip-path:polygon(0 0,92% 0,100% 50%,92% 100%,0 100%,8% 50%)}
.flow-step:first-child .step-head{clip-path:polygon(0 0,92% 0,100% 50%,92% 100%,0 100%)}
.step-head .num{font-size:11px;color:var(--red);line-height:1.1}
.step-img{height:100px;margin:14px 10px 0}
.step-text{font-size:11px;color:var(--sub);margin:10px 10px 0;line-height:1.6}
.flow .btn-more{margin-top:24px}

/* cta */
.cta{height:250px;position:relative;color:var(--white);overflow:hidden}
.cta-bg{position:absolute;inset:0;background:linear-gradient(100deg,#161616 0%,#2a2422 55%,#5a2a24 100%)}
.cta .wrap{display:flex;align-items:center;height:250px}
.cta-copy h2{font-size:22px;font-weight:900}
.cta-copy p.sub{font-size:12px;opacity:.8}
.cta-tel{display:flex;align-items:center;gap:10px;margin-top:8px}
.cta-tel .num{font-size:50px;font-weight:900;letter-spacing:.02em;line-height:1}
.cta-hours{font-size:11px;opacity:.8;margin-top:6px}
.cta-btns{margin-left:auto;display:flex;gap:14px}
.cta-btn{width:200px;height:58px;border-radius:6px;display:flex;align-items:center;justify-content:center;gap:8px;font-size:14px;font-weight:700;line-height:1.3;text-align:center}
.cta-btn.red{background:var(--red)}
.cta-btn.green{background:var(--green)}

/* footer */
.site-footer{height:444px;background:var(--grey-bg);position:relative}
.footer-cols{display:flex;gap:30px;padding-top:46px}
.footer-col{flex:1;list-style:none}
.footer-col li{font-size:12px;padding:4px 0;display:flex;align-items:center;gap:7px}
.footer-col li::before{content:"";width:5px;height:5px;background:var(--red);border-radius:50%;flex:none}
.footer-col li.sub{padding-left:14px;color:var(--sub)}
.footer-col li.sub::before{background:#bbb}
.footer-bottom{position:absolute;left:0;right:0;bottom:0;height:46px;border-top:1px solid var(--line);background:var(--white)}
.footer-bottom .wrap{display:flex;align-items:center;justify-content:space-between;height:46px;font-size:10px;color:var(--sub)}
</style>
</head>
<body>

<header class="site-header">
  <div class="header-top">
    <a class="logo" href="#"><span class="logo-name">クモマーケット</span><span class="logo-tag">出張買取・宅配買取<br>全国対応のリユース専門店</span></a>
    <div class="header-tel">
      <svg width="24" height="24" viewBox="0 0 24 24"><path fill="#d7282f" d="M6.6 10.8a15 15 0 0 0 6.6 6.6l2.2-2.2a1 1 0 0 1 1-.25 11.4 11.4 0 0 0 3.6.57 1 1 0 0 1 1 1V20a1 1 0 0 1-1 1A17 17 0 0 1 3 4a1 1 0 0 1 1-1h3.5a1 1 0 0 1 1 1c0 1.25.2 2.45.57 3.6a1 1 0 0 1-.25 1z"/></svg>
      <div><span class="num">0120-517-302</span><small>受付時間 10:00〜19:00（年中無休）</small></div>
    </div>
    <div class="header-btns">
      <a class="btn-pill red" href="#">買取依頼フォーム</a>
      <a class="btn-pill green" href="#">TALKA@で無料査定</a>
    </div>
  </div>
  <nav class="global-nav">
    <a class="is-current" href="#">ホーム</a>
    <a href="#">買取品目・ブランド一覧</a>
    <a href="#">買取実績</a>
    <a href="#">買取の流れ</a>
    <a href="#">会社概要</a>
    <a href="#">よくある質問</a>
    <a href="#">店舗情報</a>
  </nav>
</header>

<section class="hero">
  <div class="hero-visual" role="img" aria-label="家電、楽器、家具、ブランドバッグ、カメラなど買取品目の写真を並べたコラージュ"></div>
  <div class="hero-copy">
    <h1 class="hero-title">全国から買取可能！</h1>
    <div class="hero-badges">
      <div class="hero-badge"><span class="badge-circle">宅配<br>買取</span><span class="badge-text">全国どこでも<br>送料無料！</span></div>
      <div class="hero-badge"><span class="badge-circle blue">出張<br>買取</span><span class="badge-text blue">関東エリアに<br>無料出張！</span></div>
    </div>
    <p class="hero-lead">見積・査定・キャンセルなど全て無料！<br>まずはお問い合わせください。</p>
  </div>
</section>

<section class="news">
  <div class="wrap">
    <h2 class="news-head">新着情報</h2>
    <ul class="news-list">
      <li><span class="news-date num">2019.06.12</span><span class="news-cat">お知らせ</span>夏季休業期間中も宅配買取の受付を通常通り行っております。</li>
      <li><span class="news-date num">2019.06.05</span><span class="news-cat">買取情報</span>カメラ・レンズの買取を強化中です。まとめ売りも大歓迎です。</li>
      <li><span class="news-date num">2019.05.28</span><span class="news-cat">ブログ</span>楽器を高く売るためのお手入れ方法をスタッフがご紹介します。</li>
      <li><span class="news-date num">2019.05.20</span><span class="news-cat">お知らせ</span>出張買取の対応エリアを拡大しました。お気軽にご相談ください。</li>
    </ul>
  </div>
  <a class="btn-more" href="#">もっと見る <svg width="8" height="10" viewBox="0 0 8 10"><path d="M1 1l5 4-5 4" stroke="#fff" stroke-width="2" fill="none"/></svg></a>
</section>

<section class="results">
  <h2 class="sec-title">買取実績</h2>
  <p class="sec-lead">実際に買取させて頂いたお品物の一部をご紹介します。</p>
  <div class="wrap">
    <div class="result-slider">
      <span class="slide-arrow"><svg width="8" height="10" viewBox="0 0 8 10"><path d="M6 1L2 5l4 4" stroke="#333" stroke-width="2" fill="none"/></svg></span>
      <div class="result-cards">
        <article class="result-card">
          <div class="result-img" role="img" aria-label="買取したロボット掃除機の写真" style="background:linear-gradient(160deg,#eef0f2,#b9bec4)"></div>
          <div class="result-body"><p class="result-date num">2019.06.10</p><p class="result-name">ロボット掃除機 上位モデル 付属品完備 美品</p><p class="result-price">買取価格<span class="num">29,800<small>円</small></span></p></div>
        </article>
        <article class="result-card">
          <div class="result-img" role="img" aria-label="買取した革のブランドバッグの写真" style="background:linear-gradient(160deg,#e9ded2,#8a5a3c)"></div>
          <div class="result-body"><p class="result-date num">2019.06.08</p><p class="result-name">レザー ボストンバッグ ブラウン 保存袋付き</p><p class="result-price">買取価格<span class="num">12,180<small>円</small></span></p></div>
        </article>
        <article class="result-card">
          <div class="result-img" role="img" aria-label="買取したアコースティックギターの写真" style="background:linear-gradient(160deg,#f1e6d6,#c48a4a)"></div>
          <div class="result-body"><p class="result-date num">2019.06.04</p><p class="result-name">アコースティックギター ハードケース付属</p><p class="result-price">買取価格<span class="num">352,000<small>円</small></span></p></div>
        </article>
        <article class="result-card">
          <div class="result-img" role="img" aria-label="買取したコレクション雑貨の写真" style="background:linear-gradient(160deg,#efe8e2,#a7938a)"></div>
          <div class="result-body"><p class="result-date num">2019.06.01</p><p class="result-name">コレクション雑貨 まとめ 箱付き 状態良好</p><p class="result-price">買取価格<span class="num">8,500<small>円</small></span></p></div>
        </article>
      </div>
      <span class="slide-arrow"><svg width="8" height="10" viewBox="0 0 8 10"><path d="M2 1l4 4-4 4" stroke="#333" stroke-width="2" fill="none"/></svg></span>
    </div>
    <div class="dots"><span class="on"></span><span></span><span></span><span></span></div>
  </div>
  <a class="btn-more" href="#">もっと見る <svg width="8" height="10" viewBox="0 0 8 10"><path d="M1 1l5 4-5 4" stroke="#fff" stroke-width="2" fill="none"/></svg></a>
</section>

<section class="items">
  <h2 class="sec-title">買取品目・ブランド一覧</h2>
  <p class="sec-lead">幅広い商品に対応！分からない品目もまずはお気軽にご相談ください。</p>
  <div class="wrap">
    <div class="item-grid">
      <div class="item-card"><p class="item-label"><i></i>家電・AV機器・カメラ</p><div class="item-body"><p class="item-words">テレビ、冷蔵庫、洗濯機、掃除機、オーディオ、スピーカー、カメラ、レンズ</p><div class="item-img" role="img" aria-label="家電とカメラの写真" style="background:linear-gradient(#eceff2,#b8c0c8)"></div></div></div>
      <div class="item-card"><p class="item-label"><i></i>スマホ・PC関連</p><div class="item-body"><p class="item-words">Velio、Velitab、スマートフォン、タブレット、パソコン、モニター、プリンター</p><div class="item-img" role="img" aria-label="スマートフォンとパソコンの写真" style="background:linear-gradient(#eef0f2,#9aa3ad)"></div></div></div>
      <div class="item-card"><p class="item-label"><i></i>インテリア・家具・住宅設備</p><div class="item-body"><p class="item-words">テレビ台、チェア、ソファ、ベッド、照明器具、食器、調理器具</p><div class="item-img" role="img" aria-label="ソファと照明の写真" style="background:linear-gradient(#f3ece4,#c9a98a)"></div></div></div>
      <div class="item-card"><p class="item-label"><i></i>カー用品</p><div class="item-body"><p class="item-words">ヘルメット、タイヤ、ホイール、カーナビ、車載工具、自動車用機械</p><div class="item-img" role="img" aria-label="ホイールとヘルメットの写真" style="background:linear-gradient(#eeeeee,#7d7d7d)"></div></div></div>
      <div class="item-card"><p class="item-label"><i></i>ホビー</p><div class="item-body"><p class="item-words">フィギュア、ドール、トレーディングカード、プラモデル、ミニカー、鉄道模型</p><div class="item-img" role="img" aria-label="フィギュアとプラモデルの写真" style="background:linear-gradient(#f4ece6,#c58b6e)"></div></div></div>
      <div class="item-card"><p class="item-label"><i></i>ビューティ・ヘルスケア</p><div class="item-body"><p class="item-words">美顔器、ヘアケア家電、マッサージ機、健康器具</p><div class="item-img" role="img" aria-label="美顔器とヘアドライヤーの写真" style="background:linear-gradient(#f9ecef,#e0aab7)"></div></div></div>
      <div class="item-card"><p class="item-label"><i></i>ブランドファッション</p><div class="item-body"><p class="item-words">メンズ服、レディース服、時計、貴金属、アクセサリー、バッグ、財布</p><div class="item-img" role="img" aria-label="バッグと腕時計の写真" style="background:linear-gradient(#f4ebe0,#b07a46)"></div></div></div>
      <div class="item-card"><p class="item-label"><i></i>楽器</p><div class="item-body"><p class="item-words">ギター、ベース、ドラム、サックス、ピアノ、アンプ、音楽機材</p><div class="item-img" role="img" aria-label="ギターとアンプの写真" style="background:linear-gradient(#f1e7da,#a0683a)"></div></div></div>
      <div class="item-card"><p class="item-label"><i></i>美術品・雑貨</p><div class="item-body"><p class="item-words">絵画、古銭、切手、工芸品、骨董品、彫刻仏像、刀、万年筆</p><div class="item-img" role="img" aria-label="骨董品と工芸品の写真" style="background:linear-gradient(#efe9df,#8f7b5e)"></div></div></div>
      <div class="item-card"><p class="item-label"><i></i>スポーツ・アウトドア</p><div class="item-body"><p class="item-words">キャンプ、登山、釣具、ゴルフ、自転車、スノーボード、バックパック</p><div class="item-img" role="img" aria-label="キャンプ用品とゴルフ用品の写真" style="background:linear-gradient(#e8efe6,#6f8f62)"></div></div></div>
      <div class="item-card"><p class="item-label"><i></i>電動工具・機械</p><div class="item-body"><p class="item-words">DIY工具、プロ用工具、発電機、溶接機、コンプレッサー、工具箱</p><div class="item-img" role="img" aria-label="電動工具の写真" style="background:linear-gradient(#f2eee2,#c9a13c)"></div></div></div>
      <div class="item-card"><p class="item-label"><i></i>店舗・オフィス用品</p><div class="item-body"><p class="item-words">複合機、券売機、業務用冷蔵庫、製氷機、製麺機、厨房機器</p><div class="item-img" role="img" aria-label="業務用厨房機器と複合機の写真" style="background:linear-gradient(#eef0f1,#a6adb2)"></div></div></div>
    </div>
  </div>
  <a class="btn-more" href="#">もっと見る <svg width="8" height="10" viewBox="0 0 8 10"><path d="M1 1l5 4-5 4" stroke="#fff" stroke-width="2" fill="none"/></svg></a>
</section>

<section class="sites">
  <div class="wrap">
    <p class="sites-head">こちらのサイトでも高価買取中！<span>各ジャンルに特化した専門店</span></p>
    <div class="site-row">
      <a class="site-card" href="#"><div class="site-img" role="img" aria-label="電動工具が並ぶ作業場の写真" style="background:linear-gradient(135deg,#6b5a44,#c7a469)"></div><p class="site-name"><i></i>ツールクモ</p><p class="site-caption">電動工具・プロ用工具<br>専門買取</p></a>
      <a class="site-card" href="#"><div class="site-img" role="img" aria-label="トイガンコレクションの写真" style="background:linear-gradient(135deg,#3a3a3a,#8b7f6c)"></div><p class="site-name"><i></i>ガンクモ</p><p class="site-caption">トイガン・エアガン<br>専門買取</p></a>
      <a class="site-card" href="#"><div class="site-img" role="img" aria-label="ギターなど楽器の写真" style="background:linear-gradient(135deg,#5a3422,#c98a4d)"></div><p class="site-name"><i></i>ミモザオト</p><p class="site-caption">楽器・音楽機材<br>専門買取</p></a>
      <a class="site-card" href="#"><div class="site-img" role="img" aria-label="山とアウトドア用品の写真" style="background:linear-gradient(135deg,#2e6f93,#9cc7d8)"></div><p class="site-name"><i></i>ソラノハラ</p><p class="site-caption">アウトドア・スポーツ用品<br>専門買取</p></a>
      <a class="site-card" href="#"><div class="site-img" role="img" aria-label="工場機械と重機の写真" style="background:linear-gradient(135deg,#c86a1e,#e9b04a)"></div><p class="site-name"><i></i>クモマシン</p><p class="site-caption">工場機械・車両<br>専門買取</p></a>
    </div>
  </div>
</section>

<section class="flow">
  <h2 class="sec-title">買取の流れ</h2>
  <p class="sec-lead">お客様のご都合に合わせて選べる買取方法をご用意しております。</p>
  <div class="wrap">
    <div class="flow-tabs"><span class="flow-tab is-active">宅配買取</span><span class="flow-tab other">出張買取</span></div>
    <div class="flow-steps">
      <div class="flow-step"><p class="step-head"><span class="num">STEP.1</span>電話かメールで申込み</p><div class="step-img" role="img" aria-label="電話で申し込む様子のイラスト" style="background:linear-gradient(#ffffff,#dfe6ee)"></div><p class="step-text">フリーダイヤルまたはフォームからお申込みください。梱包キットをお届けします。</p></div>
      <div class="flow-step"><p class="step-head"><span class="num">STEP.2</span>ご希望の方法で発送</p><div class="step-img" role="img" aria-label="配送トラックのイラスト" style="background:linear-gradient(#ffffff,#e4e9d8)"></div><p class="step-text">お品物を梱包して発送してください。送料は全国どこでも無料です。</p></div>
      <div class="flow-step"><p class="step-head"><span class="num">STEP.3</span>専門バイヤーが査定</p><div class="step-img" role="img" aria-label="段ボールの品物を査定するイラスト" style="background:linear-gradient(#ffffff,#efe4d2)"></div><p class="step-text">到着後、専門バイヤーが丁寧に査定し結果をご連絡いたします。</p></div>
      <div class="flow-step"><p class="step-head"><span class="num">STEP.4</span>その場でお振込</p><div class="step-img" role="img" aria-label="代金を受け取る様子のイラスト" style="background:linear-gradient(#ffffff,#e2e7ef)"></div><p class="step-text">査定額にご納得いただけましたら、すぐにお振込みいたします。</p></div>
    </div>
  </div>
  <a class="btn-more" href="#">詳しく見る <svg width="8" height="10" viewBox="0 0 8 10"><path d="M1 1l5 4-5 4" stroke="#fff" stroke-width="2" fill="none"/></svg></a>
</section>

<section class="cta">
  <div class="cta-bg" role="img" aria-label="店舗外観の写真を暗くした背景"></div>
  <div class="wrap">
    <div class="cta-copy">
      <h2>無料査定とお問い合わせはお気軽に</h2>
      <p class="sub">専門スタッフが丁寧にご対応いたします</p>
      <p class="cta-tel"><svg width="40" height="40" viewBox="0 0 24 24"><path fill="#fff" d="M6.6 10.8a15 15 0 0 0 6.6 6.6l2.2-2.2a1 1 0 0 1 1-.25 11.4 11.4 0 0 0 3.6.57 1 1 0 0 1 1 1V20a1 1 0 0 1-1 1A17 17 0 0 1 3 4a1 1 0 0 1 1-1h3.5a1 1 0 0 1 1 1c0 1.25.2 2.45.57 3.6a1 1 0 0 1-.25 1z"/></svg><span class="num">0120-517-302</span></p>
      <p class="cta-hours">受付時間 10:00〜19:00（年中無休）</p>
    </div>
    <div class="cta-btns">
      <a class="cta-btn red" href="#"><svg width="20" height="16" viewBox="0 0 20 16"><rect x="1" y="1" width="18" height="14" rx="1" fill="none" stroke="#fff" stroke-width="2"/><path d="M1 2l9 7 9-7" fill="none" stroke="#fff" stroke-width="2"/></svg>買取依頼フォーム</a>
      <a class="cta-btn green" href="#">かんたんTALKA@査定<br>24時間受付中</a>
    </div>
  </div>
</section>

<footer class="site-footer">
  <div class="wrap">
    <div class="footer-cols">
      <ul class="footer-col"><li>ホーム</li><li>買取実績</li><li>買取の流れ</li><li class="sub">宅配買取</li><li class="sub">出張買取</li><li class="sub">店頭買取</li></ul>
      <ul class="footer-col"><li>買取品目・ブランド一覧</li><li class="sub">家電・AV機器・カメラ</li><li class="sub">スマホ・PC関連</li><li class="sub">インテリア・家具</li><li class="sub">ホビー</li><li class="sub">ブランドファッション</li><li class="sub">楽器</li></ul>
      <ul class="footer-col"><li class="sub">カー用品</li><li class="sub">美術品・雑貨</li><li class="sub">スポーツ・アウトドア</li><li class="sub">電動工具・機械</li><li class="sub">店舗・オフィス用品</li></ul>
      <ul class="footer-col"><li>無料査定</li><li>買取依頼フォーム</li><li>よくある質問</li><li>記事一覧</li><li>お問い合わせ</li></ul>
      <ul class="footer-col"><li>会社概要</li><li>店舗情報</li><li>プライバシーポリシー</li></ul>
    </div>
  </div>
  <div class="footer-bottom"><div class="wrap"><span>古物商許可番号 第000000000000号</span><span>Copyright © クモマーケット All Rights Reserved.</span></div></div>
</footer>

</body>
</html>
```